Harbor City Tech Service, Technology & Security Co.

need a new business card design for our Technology & Security Company. We are a Computer Networking Company, Security Camera Installers, Phone Systems.

Target Market(s)

Construction, Medical, Law Offices, Accounting, Retail etc.

Industry/Entity Type

Information Technology

Logo is attached, colors are Blue, Red, Black. Blue for Technology & Red is for Security Cameras, Access Control, Alarm Systems

Colors
fbed22
ec1f27
0555a3
ffffff

Requirements
Must have
• Pictures or Icons for
• For Technology:
• Computer, Network, Phone System, Copier, TV, Cabling
• For Security:
• Video Surveillance, Access Control, Intercom, Fire Alarm, Burglar Alarm, Time Clock

```html
<!DOCTYPE html>
<html lang="en">
<head>
<meta charset="utf-8">
<title>Harbor City Tech Service – Business Card</title>
<link href="https://fonts.googleapis.com/css2?family=Open+Sans:wght@400;600;800&display=swap" rel="stylesheet">
<style>
  :root {
    --backdrop: #dcdbdb;
    --card-dark: #231f20;
    --card-light: #f4f4f4;
    --tech-blue: #0a6ab8;
    --security-red: #ec1f27;
    --ink: #1c1c1c;
    --muted-blue: #2b5ea7;
    --white: #ffffff;
  }
  * { box-sizing: border-box; margin: 0; padding: 0; }
  html, body { width: 1200px; height: 900px; overflow: hidden; }
  body {
    background: var(--backdrop);
    font-family: "Open Sans", Arial, sans-serif;
    position: relative;
  }
  .card {
    position: absolute;
    left: 250px;
    width: 700px;
    height: 400px;
    border-radius: 22px;
  }
  /* ---------- Back side ---------- */
  .card--back { top: 30px; background: var(--card-dark); color: var(--white); }
  .service-grid {
    position: absolute;
    left: 30px; top: 30px;
    display: grid;
    grid-template-columns: repeat(6, 100px);
    gap: 14px 8px;
  }
  .tile {
    height: 122px;
    border: 3px solid var(--tile-color);
    display: flex;
    flex-direction: column;
  }
  .tile--tech { --tile-color: var(--tech-blue); }
  .tile--security { --tile-color: var(--security-red); }
  .tile__icon {
    flex: 1;
    display: flex; align-items: center; justify-content: center;
  }
  .tile__icon svg { width: 44px; height: 44px; fill: none; stroke: var(--tile-color); stroke-width: 2.4; stroke-linecap: round; stroke-linejoin: round; }
  .tile__label {
    background: var(--tile-color);
    height: 50px;
    display: flex; align-items: center; justify-content: center;
    text-align: center;
    font-size: 14px; line-height: 1.05;
    color: var(--white);
  }
  .brand {
    display: flex; align-items: center; gap: 8px;
    font-weight: 800;
    letter-spacing: -0.3px;
    text-transform: uppercase;
  }
  .brand__dot { width: 12px; height: 12px; border-radius: 50%; background: var(--security-red); }
  .card--back .brand { position: absolute; left: 34px; bottom: 34px; font-size: 20px; color: var(--white); }
  .card--back .site { position: absolute; right: 34px; bottom: 36px; font-size: 16px; color: var(--tech-blue); }
  .card--back .site span { color: var(--security-red); }
  /* ---------- Front side ---------- */
  .card--front { top: 470px; background: linear-gradient(135deg, var(--white), var(--card-light)); color: var(--ink); }
  .card--front .brand { position: absolute; right: 40px; top: 48px; font-size: 30px; color: var(--ink); }
  .person { position: absolute; left: 44px; top: 228px; }
  .person__name { font-size: 38px; font-weight: 400; letter-spacing: -0.5px; line-height: 1; }
  .person__title { font-size: 17px; color: var(--tech-blue); margin-top: 4px; }
  .divider { position: absolute; left: 44px; right: 40px; top: 310px; height: 4px; background: var(--security-red); }
  .contacts {
    position: absolute; left: 44px; right: 40px; top: 330px;
    display: flex; justify-content: space-between;
    list-style: none; font-size: 17px;
  }
  .contacts li { display: flex; align-items: center; gap: 8px; }
  .contacts svg { width: 20px; height: 20px; fill: none; stroke: var(--tech-blue); stroke-width: 2; }
</style>
</head>
<body>

<section class="card card--back" aria-label="Card back: services">
  <div class="service-grid">
    <div class="tile tile--tech"><div class="tile__icon"><svg viewBox="0 0 48 48"><rect x="4" y="8" width="30" height="22"/><path d="M14 38h10M19 30v8"/><rect x="36" y="14" width="9" height="24"/></svg></div><div class="tile__label">Computer</div></div>
    <div class="tile tile--tech"><div class="tile__icon"><svg viewBox="0 0 48 48"><circle cx="24" cy="24" r="18"/><ellipse cx="24" cy="24" rx="8" ry="18"/><path d="M6 24h36M10 14h28M10 34h28"/></svg></div><div class="tile__label">Network</div></div>
    <div class="tile tile--tech"><div class="tile__icon"><svg viewBox="0 0 48 48"><rect x="15" y="6" width="18" height="36" rx="3"/><path d="M21 36h6"/></svg></div><div class="tile__label">Phone<br>System</div></div>
    <div class="tile tile--tech"><div class="tile__icon"><svg viewBox="0 0 48 48"><rect x="14" y="6" width="20" height="10"/><rect x="6" y="16" width="36" height="16" rx="2"/><rect x="14" y="26" width="20" height="14"/></svg></div><div class="tile__label">Copier</div></div>
    <div class="tile tile--tech"><div class="tile__icon"><svg viewBox="0 0 48 48"><rect x="4" y="8" width="40" height="26"/><path d="M16 40h16M24 34v6"/></svg></div><div class="tile__label">TV</div></div>
    <div class="tile tile--tech"><div class="tile__icon"><svg viewBox="0 0 48 48"><rect x="6" y="6" width="10" height="8"/><path d="M11 14v8q0 8 12 8t12 8v2"/><rect x="30" y="36" width="10" height="8"/></svg></div><div class="tile__label">Cabling</div></div>

    <div class="tile tile--security"><div class="tile__icon"><svg viewBox="0 0 48 48"><path d="M6 18l26-8 4 10-26 8z"/><path d="M20 25l4 9M36 15l6 0M8 40h20"/></svg></div><div class="tile__label">Video<br>Surveillance</div></div>
    <div class="tile tile--security"><div class="tile__icon"><svg viewBox="0 0 48 48"><circle cx="22" cy="12" r="6"/><path d="M22 12v18l-5-4-3 3 9 11h14l3-14-10-3"/></svg></div><div class="tile__label">Access<br>Control</div></div>
    <div class="tile tile--security"><div class="tile__icon"><svg viewBox="0 0 48 48"><rect x="8" y="6" width="10" height="36" rx="3"/><rect x="20" y="10" width="20" height="30" rx="2"/><path d="M25 18h10M25 25h2M30 25h2M35 25h0M25 31h2M30 31h2"/></svg></div><div class="tile__label">Intercom</div></div>
    <div class="tile tile--security"><div class="tile__icon"><svg viewBox="0 0 48 48"><circle cx="22" cy="24" r="16"/><circle cx="22" cy="24" r="6"/><path d="M38 14v20"/></svg></div><div class="tile__label">Fire Alarm</div></div>
    <div class="tile tile--security"><div class="tile__icon"><svg viewBox="0 0 48 48"><rect x="14" y="12" width="20" height="24" rx="2"/><path d="M19 18h10M19 24h10M19 30h10M8 16q-4 8 0 16M40 16q4 8 0 16"/></svg></div><div class="tile__label">Burglar<br>Alarm</div></div>
    <div class="tile tile--security"><div class="tile__icon"><svg viewBox="0 0 48 48"><circle cx="24" cy="24" r="17"/><path d="M24 13v11l8 5"/></svg></div><div class="tile__label">Time Clock</div></div>
  </div>
  <div class="brand"><span class="brand__dot"></span>Harbor City Tech Service</div>
  <p class="site">www.yourwebsite<span>.com</span></p>
</section>

<section class="card card--front" aria-label="Card front: contact details">
  <div class="brand"><span class="brand__dot"></span>Harbor City Tech Service</div>
  <div class="person">
    <h1 class="person__name">Your Name</h1>
    <p class="person__title">Job Title</p>
  </div>
  <div class="divider"></div>
  <ul class="contacts">
    <li><svg viewBox="0 0 24 24"><path d="M5 3h4l2 5-3 2a12 12 0 0 0 6 6l2-3 5 2v4a2 2 0 0 1-2 2A18 18 0 0 1 3 5a2 2 0 0 1 2-2z"/></svg>000 000 0000</li>
    <li><svg viewBox="0 0 24 24"><rect x="2" y="5" width="20" height="14"/><path d="M2 5l10 8 10-8"/></svg>youremail@xyz.com</li>
    <li><svg viewBox="0 0 24 24"><circle cx="12" cy="12" r="10"/><ellipse cx="12" cy="12" rx="4" ry="10"/><path d="M2 12h20"/></svg>www.yourwebsite.com</li>
  </ul>
</section>

</body>
</html>
```